agricultural technology company needs business cards*

design a business card that represents our business well. please see our website: vastrelbyfieldseal.com.au
professional, simple, clean lines, not complicated or floral.....

```html
<!DOCTYPE html>
<html lang="en">
<head>
<meta charset="utf-8">
<title>Vastrel ByfieldSeal – Business Card</title>
<link href="https://fonts.googleapis.com/css2?family=Roboto:wght@400;500;700&display=swap" rel="stylesheet">
<style>
  :root {
    --backdrop: #d9d9d9;
    --card-black: #1c1c1e;
    --card-charcoal: #2a2a2c;
    --navy: #17305f;
    --leaf-green: #8dc63f;
    --brand-green: #22b04b;
    --white: #ffffff;
    --soft-grey: #5a5a5e;
  }
  * { box-sizing: border-box; margin: 0; padding: 0; }
  html, body { width: 799px; height: 1200px; overflow: hidden; }
  body {
    background: var(--backdrop);
    font-family: "Roboto", Arial, sans-serif;
    display: flex;
    flex-direction: column;
    align-items: center;
    justify-content: center;
    gap: 110px;
  }
  .card {
    position: relative;
    width: 640px;
    height: 366px;
    border-radius: 4px;
    overflow: hidden;
    background: var(--card-black);
  }

  /* Front side */
  .card-front {
    display: flex;
    align-items: center;
    justify-content: center;
  }
  .front-wordmark {
    display: flex;
    align-items: center;
    gap: 18px;
  }
  .front-wordmark .mark-square {
    width: 34px;
    height: 34px;
    background: var(--soft-grey);
  }
  .front-wordmark .brand-name {
    font-weight: 700;
    font-size: 40px;
    letter-spacing: -0.5px;
    color: var(--soft-grey);
  }

  /* Back side */
  .card-back { background: var(--card-charcoal); }
  .back-header {
    position: absolute;
    top: 26px;
    left: 28px;
    display: flex;
    align-items: center;
    gap: 12px;
  }
  .back-header .brand-name {
    font-weight: 700;
    font-size: 30px;
    letter-spacing: -0.3px;
    color: var(--white);
  }
  .back-header .mark-square {
    width: 22px;
    height: 22px;
    background: var(--brand-green);
  }
  .navy-panel {
    position: absolute;
    inset: 0;
    background: var(--navy);
    clip-path: polygon(0 22%, 66% 22%, 100% 100%, 0 100%);
  }
  .contact-block {
    position: absolute;
    left: 34px;
    top: 108px;
    color: var(--white);
  }
  .person-name {
    font-weight: 700;
    font-size: 21px;
    color: var(--leaf-green);
  }
  .person-role {
    font-size: 14px;
    margin-top: 2px;
    margin-bottom: 16px;
  }
  .contact-list { list-style: none; }
  .contact-list li {
    display: flex;
    align-items: center;
    gap: 10px;
    font-size: 15px;
    line-height: 26px;
  }
  .contact-list svg { width: 13px; height: 13px; fill: var(--leaf-green); flex: none; }
  .contact-list .address { padding-left: 0; }
</style>
</head>
<body>

  <section class="card card-front" aria-label="Card front">
    <div class="front-wordmark">
      <span class="mark-square"></span>
      <span class="brand-name">Vastrel ByfieldSeal</span>
    </div>
  </section>

  <section class="card card-back" aria-label="Card back">
    <div class="back-header">
      <span class="brand-name">Vastrel ByfieldSeal</span>
      <span class="mark-square"></span>
    </div>
    <div class="navy-panel"></div>
    <div class="contact-block">
      <p class="person-name">Jory Van Aswegen</p>
      <p class="person-role">Managing Director</p>
      <ul class="contact-list">
        <li>
          <svg viewBox="0 0 24 24" aria-hidden="true"><path d="M6.6 10.8a15.1 15.1 0 0 0 6.6 6.6l2.2-2.2a1 1 0 0 1 1-.25 11.4 11.4 0 0 0 3.6.57 1 1 0 0 1 1 1V20a1 1 0 0 1-1 1A17 17 0 0 1 3 4a1 1 0 0 1 1-1h3.5a1 1 0 0 1 1 1c0 1.25.2 2.45.57 3.57a1 1 0 0 1-.25 1z"/></svg>
          1300 482 610
        </li>
        <li>
          <svg viewBox="0 0 24 24" aria-hidden="true"><path d="M2 5h20v14H2z M2 5l10 8 10-8" /><path d="M3 6l9 7 9-7" fill="var(--navy)"/></svg>
          jory@vastrelbyfieldseal.com.au
        </li>
        <li>
          <svg viewBox="0 0 24 24" aria-hidden="true"><circle cx="12" cy="12" r="10"/><path d="M2 12h20M12 2c3 3 3 17 0 20M12 2c-3 3-3 17 0 20" stroke="var(--navy)" stroke-width="1.6" fill="none"/></svg>
          www.vastrelbyfieldseal.com.au
        </li>
        <li class="address">52 Tallis Road, Kwinana, WA 6167</li>
      </ul>
    </div>
  </section>

</body>
</html>
```